Adventure Business Cards

Please check out our website for style
Vertical card
Details:
Side 1
Logo
Business name: Kestrel Point Wildland Tours
Name: Colin Warbeck
Role: Director
Email: info@kestrelpointtours.com
Address: PO Box 71, Marlin Cove NSW 2471
Phone: +61 2 5550 1847
Web address: www.kestrelpointtours.com
Side 2
Taking pictures?
A Friendwall and Pixlane logo
Tag us in your pictures with
#kpwildtours
@kpwildtours
www.kestrelpointtours.com
Details:
Side 1
Logo
Name: Colin Warbeck
Role: Director
Phone: +61 2 5550 1847
Side 2
Taking pictures?
#kpwildtours
@kpwildtours

```html
<!DOCTYPE html>
<html lang="en">
<head>
<meta charset="utf-8">
<title>Kestrel Point Wildland Tours – Business Cards</title>
<link rel="stylesheet" href="https://fonts.googleapis.com/css2?family=Open+Sans:wght@400;600;700;800&display=swap">
<style>
  :root {
    --ink: #111111;
    --paper: #ffffff;
    --gold: #f2c318;
    --gold-deep: #e0ac0b;
    --navy: #1d2a3a;
    --reef-dark: #17393d;
    --reef-mid: #2d6467;
    --reef-light: #5f9690;
    --social-blue: #3a5a98;
    --backdrop: #dcd7cf;
    --muted: #3a3a3a;
  }
  * { box-sizing: border-box; margin: 0; padding: 0; }
  html, body { width: 1200px; height: 780px; overflow: hidden; }
  body {
    background: var(--backdrop);
    font-family: "Open Sans", Verdana, sans-serif;
    position: relative;
  }
  .card {
    position: absolute;
    top: 110px;
    width: 340px;
    height: 560px;
    overflow: hidden;
    box-shadow: 0 10px 28px rgba(0,0,0,.22);
  }
  .card--front { left: 220px; background: var(--ink); }
  .card--back { left: 640px; }

  .front-shape { position: absolute; inset: 0; }

  .brand {
    position: absolute;
    display: flex;
    align-items: center;
    gap: 10px;
  }
  .brand__disc {
    flex: none;
    border-radius: 50%;
    background: var(--navy);
  }
  .brand__name {
    font-weight: 700;
    line-height: 1.15;
    text-transform: uppercase;
    letter-spacing: .04em;
  }
  .card--front .brand { top: 96px; right: 22px; flex-direction: row-reverse; }
  .card--front .brand__disc { width: 78px; height: 78px; }
  .card--front .brand__name { color: var(--navy); font-size: 12px; text-align: right; width: 120px; }

  .contact { position: absolute; left: 28px; top: 215px; color: var(--ink); }
  .contact__name { color: var(--gold); font-weight: 800; font-size: 26px; line-height: 1.05; }
  .contact__role { font-weight: 700; font-size: 15px; margin-bottom: 12px; }
  .contact__address { font-size: 15px; line-height: 1.3; margin-bottom: 8px; }
  .contact__row { display: flex; align-items: center; gap: 8px; font-size: 14px; line-height: 1.55; }
  .contact__icon {
    width: 16px; height: 16px; background: var(--gold);
    display: flex; align-items: center; justify-content: center; flex: none;
  }
  .contact__icon svg { width: 11px; height: 11px; }

  .front-web {
    position: absolute; left: 0; right: 0; bottom: 40px;
    text-align: center; color: var(--paper); font-size: 16px; letter-spacing: .03em;
  }

  .reef-photo {
    position: absolute; inset: 0;
    background:
      radial-gradient(ellipse at 60% 45%, rgba(214,190,160,.55) 0%, rgba(214,190,160,0) 38%),
      linear-gradient(160deg, var(--reef-light) 0%, var(--reef-mid) 45%, var(--reef-dark) 100%);
  }
  .social-strip {
    position: absolute; left: 0; top: 0; bottom: 0; width: 54px;
    background: var(--paper);
    display: flex; flex-direction: column; justify-content: space-around; align-items: center;
    padding: 30px 0;
  }
  .social-tag {
    writing-mode: vertical-rl;
    display: flex; align-items: center; gap: 10px;
    font-size: 15px; color: var(--muted);
  }
  .social-tag__mark { width: 18px; height: 18px; background: var(--social-blue); }
  .social-tag__network { font-size: 10px; font-weight: 600; color: var(--social-blue); }

  .card--back .brand { right: 18px; bottom: 26px; }
  .card--back .brand__disc { width: 70px; height: 70px; background: var(--gold); }
  .card--back .brand__name { color: var(--paper); font-size: 12px; width: 110px; }
</style>
</head>
<body>

<section class="card card--front" aria-label="Business card, front">
  <svg class="front-shape" viewBox="0 0 340 560" preserveAspectRatio="none" aria-hidden="true">
    <path d="M0,82 Q170,48 340,92" fill="none" stroke="var(--gold)" stroke-width="7"/>
    <path d="M0,96 Q170,62 340,106" fill="none" stroke="var(--gold)" stroke-width="4"/>
    <path d="M0,106 Q170,72 340,116 L340,440 Q170,500 0,445 Z" fill="var(--paper)"/>
    <path d="M0,449 Q170,504 340,444" fill="none" stroke="var(--gold)" stroke-width="6"/>
  </svg>

  <div class="brand">
    <span class="brand__disc"></span>
    <span class="brand__name">Kestrel Point Wildland Tours</span>
  </div>

  <div class="contact">
    <p class="contact__name">Colin Warbeck</p>
    <p class="contact__role">Director</p>
    <p class="contact__address">PO Box 71, Marlin Cove<br>NSW 2471</p>
    <p class="contact__row">
      <span class="contact__icon"><svg viewBox="0 0 12 12"><path d="M2.5 1h2l1 2.5-1.3 1a6 6 0 0 0 3.3 3.3l1-1.3 2.5 1v2a1 1 0 0 1-1 1A9 9 0 0 1 1.5 2a1 1 0 0 1 1-1z" fill="#fff"/></svg></span>
      +61 2 5550 1847
    </p>
    <p class="contact__row">
      <span class="contact__icon"><svg viewBox="0 0 12 12"><rect x="1" y="2.5" width="10" height="7" fill="none" stroke="#fff" stroke-width="1.2"/><path d="M1 3l5 3.5L11 3" fill="none" stroke="#fff" stroke-width="1.2"/></svg></span>
      info@kestrelpointtours.com
    </p>
  </div>

  <p class="front-web">www.kestrelpointtours.com</p>
</section>

<section class="card card--back" aria-label="Business card, back">
  <div class="reef-photo" role="img" aria-label="Underwater photograph of a striped lionfish swimming over a reef"></div>

  <div class="social-strip">
    <p class="social-tag"><span class="social-tag__mark"></span><span class="social-tag__network">Friendwall</span>#kpwildtours</p>
    <p class="social-tag"><span class="social-tag__mark"></span><span class="social-tag__network">Pixlane</span>@kpwildtours</p>
  </div>

  <div class="brand">
    <span class="brand__name">Kestrel Point Wildland Tours</span>
    <span class="brand__disc"></span>
  </div>
</section>

</body>
</html>
```